Herbal Apothecary Rebrand

I am in the process of merging two companies Wren Hollow Oils and Under The Pines Apothecary. I am dissolving Wren Hollow Oils (WHO) and need to blend a few of the products into the Under The Pines Apothecary (UTP) line. These blended products will take on a fresh new look. This is where I need some help. I have a few ideas but need some creative genius to bring them together.
The following products need to be merged and once a logo is agreed upon I will be working with this designer with further pay to create the following:
~ body oils (labels and packaging) **existing product shown in image A-1
~ plant bath medicines (labels and packaging) **a new product with the bottle and packaging shown in images attached
~ facial serum (labels and packaging - the packaging will be the same cardboard boxes used for the body oils) **existing product shown in
image A-2
~ teas (labeling) **a new product - packaging sample pics attached
~ as well as having the ability to carry over into the creation of 40 different essential oil containers. ** An idea I have is shown in image C-1.
Ideas...
I prefer distinct lines, square designs vs circular or curvy. I prefer clean and clear vs busy.
I like the layout shown in images A-1 & A-2 and could see moving forward with a very similar style without the indigenous logo. I would like to see what it looks like to have the UTP logo (building with trees) in place of the indigenous logo. ** I am open to reworking the UTP logo to make it a bit more vertical in size vs being quite small and horizontal. This could include revising or recreating the building and trees altogether.
I like the speckled background (shown in image B-1), it gives the sense that it is aged and goes with the Apothecary theme, however I'm not completely attached to it.
I like the off white labels that I currently have for the BODY OILS and the SERUM and I am leaning towards this as the colour for the new blended line. I would also be open to seeing a lighter version of the turquoise.
This is just an idea that I have however I am open to something completely new. What is important is that it blends nicely with the current line of products available at UTP (the entire line can be seen online). There is a good chance that I will be merging the products over to the new and improved design as we move through the older packaging.
Notes on Plant Bath labels:
**If working from the current layout of the Body Oil labels this can be used as an example to create a template
~ The top will have the new or reworked logo (with or without the company name depending on space available)
~ First line for each bottle will have a name eg: NETTLE + ROSE
~ Second line will be the purpose of the medicine eg: HEART OPENING
~ The next line will read: PLANT BATH
~Then space for a little blurb eg: BRINGING BALANCE TO THE EMOTIONAL AND ENERGETIC HEALTH OF THE HEART.
~ The size of the bottle will read 400 ML but in a vertical direction on the bottle
Notes on Tea labels:
The teas have not been created yet but I'm looking for some ideas that follow in the same design as the Plant Bath labels so the following can be used as an example:
~ Name; TULSI + ROSE
~ The purpose: ELEVATED HEART
~ The bottom will read: LOOSE TEA
~ Blurb about the benefits: A TRANSFORMATIONAL CREATION OF WARM NOTES WITH DEEP WOODY UNDERTONES. THIS ANYTIME TEA IS AS PLEASING IN THE HEALTH BENEFITS AS IT IS TO THE TASTE.
~ Include the size: 100g
**I maxed out in pictures so I wasn't able to add more inspiration pics but I also quite like the fern & marsh tea line (shows up in a google search) as its clean and clear. The difference being I won't be printing directly on the packaging, it will need to be a label.
Logo Text
I would like to see if we can incorporate the name UNDER THE PINES APOTHECARY however this might make it too busy. Perhaps smaller lettering for "under the pines" and larger for "APOTHECARY". It also might be the case that adding this on the front makes things look too busy. I'm open to creative suggestions.

```html
<!DOCTYPE html>
<html lang="en">
<head>
<meta charset="utf-8">
<title>Under The Pines Apothecary — Label System</title>
<link href="https://fonts.googleapis.com/css2?family=Arvo&family=Oswald:wght@400;500&family=Pathway+Gothic+One&display=swap" rel="stylesheet">
<style>
  :root {
    --ink: #2b1a14;
    --page: #ffffff;
    --band: #dcdcdc;
    --teal: #5fc7bc;
    --offwhite: #f2f1ee;
    --white: #ffffff;
    --kraft: #c39a66;
    --art-tone: #b9aca6;
  }
  * { box-sizing: border-box; margin: 0; padding: 0; }
  html, body { width: 720px; height: 1200px; overflow: hidden; background: var(--page); }
  body { position: relative; color: var(--ink); font-family: "Pathway Gothic One", sans-serif; }

  /* ---------- Brand presentation ---------- */
  .brand-showcase { position: absolute; left: 0; top: 0; width: 720px; height: 681px; background: var(--page); }
  .lockup { position: absolute; left: 215px; top: 70px; width: 290px; text-align: center; font-family: "Arvo", serif; font-weight: 400; color: var(--ink); }
  .lockup .lockup-small { display: block; font-size: 22px; letter-spacing: 7px; line-height: 1.2; }
  .lockup .lockup-large { display: block; font-size: 38px; letter-spacing: 1px; line-height: 1.25; }
  .lockup-art { position: absolute; left: 244px; top: 186px; width: 232px; height: 82px; border-radius: 3px;
    background: linear-gradient(180deg, #e6e0dd 0%, var(--art-tone) 100%); }
  .monogram { position: absolute; left: 260px; top: 380px; width: 200px; text-align: center; font-family: "Arvo", serif; font-weight: 400; color: var(--ink); }
  .monogram .mono-letters { display: block; font-size: 64px; line-height: 1; letter-spacing: 2px; }
  .monogram .mono-name { display: block; font-size: 13px; letter-spacing: 4px; margin-top: 6px; }

  /* ---------- Label sheet ---------- */
  .label-sheet { position: absolute; left: 0; top: 681px; width: 720px; height: 519px; background: var(--band); }
  .label { position: absolute; width: 300px; height: 218px; color: var(--ink); }
  .label--teal { left: 45px; top: 19px; background: var(--teal); }
  .label--offwhite { left: 374px; top: 19px; background: radial-gradient(circle at 30% 40%, #f7f6f3 0%, var(--offwhite) 70%); }
  .label--white { left: 45px; top: 262px; background: var(--white); }
  .label--kraft { left: 374px; top: 262px; background: linear-gradient(135deg, #c9a16d 0%, var(--kraft) 100%); }

  .side-notes { position: absolute; left: 14px; top: 18px; height: 184px; width: 34px; display: flex; gap: 6px;
    writing-mode: vertical-rl; transform: rotate(180deg); font-family: "Pathway Gothic One", sans-serif; font-size: 4.6px; line-height: 1.25; letter-spacing: 0.1px; }
  .side-notes p { width: auto; }
  .side-notes b { font-family: "Oswald", sans-serif; font-weight: 500; }

  .label-brand { position: absolute; left: 85px; top: 18px; width: 131px; text-align: center; font-family: "Arvo", serif; font-weight: 400; }
  .label-brand .small { display: block; font-size: 8px; letter-spacing: 2.4px; line-height: 1.3; }
  .label-brand .large { display: block; font-size: 14.5px; line-height: 1.3; }

  .label-art { position: absolute; left: 100px; top: 68px; width: 102px; height: 34px; border-radius: 2px;
    background: linear-gradient(180deg, rgba(43,26,20,0.18) 0%, rgba(43,26,20,0.42) 100%); }

  .product { position: absolute; left: 85px; top: 108px; width: 131px; }
  .product-row { border-bottom: 0.8px solid var(--ink); height: 19px; display: flex; align-items: flex-end; padding-bottom: 2px; }
  .product-name { font-family: "Oswald", sans-serif; font-weight: 500; font-size: 10px; letter-spacing: 0.3px; }
  .product-type { font-family: "Oswald", sans-serif; font-weight: 400; font-size: 10px; letter-spacing: 0.3px; }
  .product-tag { font-size: 8px; letter-spacing: 0.3px; height: 17px; }
  .product-detail { display: flex; align-items: stretch; height: 37px; border-bottom: 0.8px solid var(--ink); padding: 4px 0 2px; }
  .blurb { flex: 1; font-size: 7.4px; line-height: 1.25; letter-spacing: 0.2px; }
  .size { width: 20px; border-left: 0.8px solid var(--ink); display: flex; align-items: center; justify-content: center; }
  .size span { writing-mode: vertical-rl; transform: rotate(180deg); font-family: "Oswald", sans-serif; font-size: 9px; }

  .url-box { position: absolute; left: 243px; top: 18px; width: 44px; height: 184px; border: 0.8px solid var(--ink);
    display: flex; align-items: center; justify-content: flex-end; padding-right: 4px; }
  .url-box span { writing-mode: vertical-rl; transform: rotate(180deg); font-family: "Oswald", sans-serif; font-size: 5.6px; letter-spacing: 0.2px; }
</style>
</head>
<body>

<section class="brand-showcase">
  <div class="lockup">
    <span class="lockup-small">UNDER THE PINES</span>
    <span class="lockup-large">APOTHECARY</span>
  </div>
  <div class="lockup-art" role="img" aria-label="Ink sketch of a small cabin between pine trees"></div>
  <div class="monogram">
    <span class="mono-letters">UTP</span>
    <span class="mono-name">UNDER THE PINES</span>
  </div>
</section>

<section class="label-sheet">

  <article class="label label--teal">
    <div class="side-notes">
      <p><b>SUGGESTED USE:</b> WARM OIL IF DESIRED. APPLY TO THE FULL BODY AFTER BATHING. MASSAGE IN MOTIONS TOWARD THE HEART UNTIL THE OIL IS MOSTLY ABSORBED. CAN ALSO BE ADDED TO BATH WATER.</p>
      <p><b>INGREDIENTS:</b> SUNFLOWER OIL, ORANGE, CARDAMOM, CYPRESS, GINGER ORGANIC.</p>
    </div>
    <div class="label-brand"><span class="small">UNDER THE PINES</span><span class="large">APOTHECARY</span></div>
    <div class="label-art" role="img" aria-label="Ink sketch of a cabin among pines"></div>
    <div class="product">
      <div class="product-row"><span class="product-name">CARDAMON + CYPRESS</span></div>
      <div class="product-row"><span class="product-type">WARMING BODY OIL</span></div>
      <div class="product-row product-tag">ORGANIC BOTANICALS</div>
      <div class="product-detail">
        <p class="blurb">REVITALIZING AND<br>STIMULATING FOR A<br>RENEWED SENSE OF SPIRIT</p>
        <div class="size"><span>100ML</span></div>
      </div>
    </div>
    <div class="url-box"><span>underthepinesapothecary.com</span></div>
  </article>

  <article class="label label--offwhite">
    <div class="side-notes">
      <p><b>SUGGESTED USE:</b> WARM OIL IF DESIRED. APPLY TO THE FULL BODY AFTER BATHING. MASSAGE IN MOTIONS TOWARD THE HEART UNTIL THE OIL IS MOSTLY ABSORBED. CAN ALSO BE ADDED TO BATH WATER.</p>
      <p><b>INGREDIENTS:</b> SUNFLOWER OIL, ORANGE, CARDAMOM, CYPRESS, GINGER ORGANIC.</p>
    </div>
    <div class="label-brand"><span class="small">UNDER THE PINES</span><span class="large">APOTHECARY</span></div>
    <div class="label-art" role="img" aria-label="Ink sketch of a cabin among pines"></div>
    <div class="product">
      <div class="product-row"><span class="product-name">NETTLE + ROSE</span></div>
      <div class="product-row"><span class="product-type">PLANT BATH</span></div>
      <div class="product-row product-tag">ORGANIC BOTANICALS</div>
      <div class="product-detail">
        <p class="blurb">BRINGING BALANCE TO THE<br>EMOTIONAL AND ENERGETIC<br>HEALTH OF THE HEART</p>
        <div class="size"><span>400ML</span></div>
      </div>
    </div>
    <div class="url-box"><span>underthepinesapothecary.com</span></div>
  </article>

  <article class="label label--white">
    <div class="side-notes">
      <p><b>SUGGESTED USE:</b> WARM OIL IF DESIRED. APPLY TO THE FULL BODY AFTER BATHING. MASSAGE IN MOTIONS TOWARD THE HEART UNTIL THE OIL IS MOSTLY ABSORBED. CAN ALSO BE ADDED TO BATH WATER.</p>
      <p><b>INGREDIENTS:</b> SUNFLOWER OIL, ORANGE, CARDAMOM, CYPRESS, GINGER ORGANIC.</p>
    </div>
    <div class="label-brand"><span class="small">UNDER THE PINES</span><span class="large">APOTHECARY</span></div>
    <div class="label-art" role="img" aria-label="Ink sketch of a cabin among pines"></div>
    <div class="product">
      <div class="product-row"><span class="product-name">TULSI + ROSE</span></div>
      <div class="product-row"><span class="product-type">LOOSE TEA</span></div>
      <div class="product-row product-tag">ORGANIC BOTANICALS</div>
      <div class="product-detail">
        <p class="blurb">A TRANSFORMATIONAL<br>CREATION OF WARM NOTES<br>WITH DEEP WOODY UNDERTONES.</p>
        <div class="size"><span>100g</span></div>
      </div>
    </div>
    <div class="url-box"><span>underthepinesapothecary.com</span></div>
  </article>

  <article class="label label--kraft">
    <div class="side-notes">
      <p><b>SUGGESTED USE:</b> WARM OIL IF DESIRED. APPLY TO THE FULL BODY AFTER BATHING. MASSAGE IN MOTIONS TOWARD THE HEART UNTIL THE OIL IS MOSTLY ABSORBED. CAN ALSO BE ADDED TO BATH WATER.</p>
      <p><b>INGREDIENTS:</b> SUNFLOWER OIL, ORANGE, CARDAMOM, CYPRESS, GINGER ORGANIC.</p>
    </div>
    <div class="label-brand"><span class="small">UNDER THE PINES</span><span class="large">APOTHECARY</span></div>
    <div class="label-art" role="img" aria-label="Ink sketch of a cabin among pines"></div>
    <div class="product">
      <div class="product-row"><span class="product-name">NETTLE + ROSE</span></div>
      <div class="product-row"><span class="product-type">PLANT BATH</span></div>
      <div class="product-row product-tag">ORGANIC BOTANICALS</div>
      <div class="product-detail">
        <p class="blurb">BRINGING BALANCE TO THE<br>EMOTIONAL AND ENERGETIC<br>HEALTH OF THE HEART</p>
        <div class="size"><span>400ML</span></div>
      </div>
    </div>
    <div class="url-box"><span>underthepinesapothecary.com</span></div>
  </article>

</section>

</body>
</html>
```